Business Cards, 2 Trifold Brochures
Plumvault
Professional
Darren K. Whitlow
VP Business Development
482 Haverlund Corporate Park
darren@plumvault.example
http://www.plumvault.example
Need two separate tri-fold brochure designs.
Brochure A: Will be handed out to potential customers, should have similar look and feel as our website (www.plumvault.example). Brochure should summarize the benefits of using a remote managed backup solution.
Brochure B: Will be for potential resellers of PlumVault Service. Should summarize benefits of offering a remotely managed backup solution to their customers, creates additional income stream, profit sharing/very lucrative, will increase their marketability , backup solution has huge benefit to customer, how they can easily market to their existing customer base, and that Plumvault will fully train and support them etc.
•256 bit encryption for ultimate security
•Fast online recovery of any version of any protected file
•Easy Installation and setup
•Completely automated offsite-protection
•High speed internet is all that is required.

```html
<!DOCTYPE html>
<html lang="en">
<head>
<meta charset="utf-8">
<title>PlumVault Trifold Brochure</title>
<link href="https://fonts.googleapis.com/css2?family=Arimo:wght@400;700&display=swap" rel="stylesheet">
<style>
:root{
  --bg:#e9e6e1;
  --ink:#222;
  --dark:#141414;
  --dark2:#3a3a3a;
  --yellow:#f6b90a;
  --yellow2:#ffd54a;
  --blue:#1b4f94;
  --red:#c8141f;
  --orange:#e07b00;
  --link:#2a5db0;
  --panel:#ffffff;
}
*{box-sizing:border-box;margin:0;padding:0}
html,body{width:1200px;height:929px;overflow:hidden;background:var(--bg);font-family:"Arimo",Arial,sans-serif;color:var(--ink)}
.stage{width:1200px;height:929px;display:flex;flex-direction:column;align-items:center;justify-content:center;gap:18px}
.spread{width:660px;height:440px;display:flex;background:var(--panel);box-shadow:0 3px 10px rgba(0,0,0,.25)}
.panel{width:220px;height:100%;display:flex;flex-direction:column;border-right:1px solid #cfcfcf;position:relative;overflow:hidden}
.panel:last-child{border-right:none}
.head{height:30px;flex:none;background:linear-gradient(#4a4a4a,var(--dark));display:flex;align-items:center;padding:0 8px;gap:6px}
.tab{background:linear-gradient(var(--yellow2),var(--yellow));color:var(--dark);font-size:9px;font-weight:700;padding:4px 10px;border-radius:2px}
.tab.dark{background:none;color:#fff;padding:0}
.tab.dark b{color:var(--yellow)}
.dot{width:18px;height:18px;border-radius:50%;background:#fff;border:3px solid var(--yellow)}
.body{flex:1;padding:7px 10px;font-size:6.2px;line-height:1.45;overflow:hidden}
.body h3{font-size:8px;color:var(--blue);margin:3px 0 2px}
.body h4{font-size:6.8px;color:var(--orange);margin:4px 0 1px}
.body p{margin-bottom:3px}
.links{list-style:none;margin-top:5px}
.links li{color:var(--link);border-bottom:1px dotted #aaa;padding:2px 0;font-size:6.2px}
.photo{height:120px;background:linear-gradient(135deg,#cfd6de,#8a97a6 60%,#5d6877);margin:4px 0;border:2px solid #fff;box-shadow:0 0 0 1px #bbb}
.band{height:46px;flex:none;background:linear-gradient(var(--yellow2),var(--yellow));padding:6px 10px;display:flex;flex-direction:column;justify-content:center}
.band .small{font-size:8px;font-weight:700;color:var(--dark)}
.band .big{font-size:13px;font-weight:700;color:#fff;letter-spacing:.5px}
.band.black{background:linear-gradient(#333,var(--dark))}
.band.black .small{color:#fff}
.band.black .big{color:var(--yellow)}
.mid{background:linear-gradient(#5a5a5a,#2b2b2b)}
.mid .body{color:#fff}
.bullets{list-style:none;font-size:6.8px;font-weight:700}
.bullets li{display:flex;gap:4px;align-items:flex-start;margin-bottom:6px}
.bullets li::before{content:"";width:5px;height:5px;background:var(--yellow);margin-top:2px;flex:none}
.contact{background:#fff;color:var(--ink);padding:8px;margin-top:8px;border-left:4px solid var(--yellow)}
.contact h3{color:var(--red);font-size:9px;margin:0 0 4px}
.contact .row{display:flex;gap:4px}
.contact .lbl{width:28px;font-weight:700}
.contact p{margin-top:5px}
.band .big.tollfree{font-size:16px}
.cover{background:#fff}
.cover .top{height:44px;flex:none;background:linear-gradient(#2a2a2a,var(--dark));display:flex;align-items:center;justify-content:flex-end;padding:0 12px;gap:6px}
.logo-mark{width:16px;height:16px;background:var(--yellow)}
.logo-name{font-size:17px;font-weight:700;color:#fff}
.slogan{padding:12px 12px 0;text-align:right;font-weight:700;line-height:1.1}
.slogan .s1{font-size:14px;color:var(--blue)}
.slogan .s2{font-size:18px;color:var(--red)}
.slogan .s3{font-size:13px;color:var(--blue)}
.globe-area{flex:1;margin:10px 12px 0;background:radial-gradient(ellipse at 60% 50%,#bcdcff,#4a8ad6 55%,#e8eef6 80%);border-radius:4px}
.url{font-size:8px;text-align:right;padding:6px 12px;color:var(--dark2);flex:none}
.badge-band{flex-direction:row;align-items:center;gap:8px}
.circle247{width:32px;height:32px;border-radius:50%;background:var(--dark);color:var(--yellow);font-size:11px;font-weight:700;display:flex;align-items:center;justify-content:center;flex:none}
.badge-band .small{font-size:7px;line-height:1.2}
.icons{display:grid;grid-template-columns:repeat(4,1fr);gap:5px;margin:5px 0;height:92px}
.icons span{background:linear-gradient(#f4f4f4,#cfd4da);border:1px solid #bbb}
.ticks{list-style:none}
.ticks li{display:flex;gap:4px;margin-bottom:2px}
.ticks li::before{content:"";width:4px;height:4px;background:var(--orange);margin-top:2px;flex:none}
.risk{display:flex;gap:5px;margin-bottom:3px}
.risk .sq{width:16px;height:16px;background:linear-gradient(var(--yellow2),var(--orange));flex:none;border-radius:2px}
.risk b{color:var(--orange);display:block;font-size:6.8px}
.feature{display:flex;gap:5px;margin-bottom:3px}
.feature .sq{width:14px;height:14px;background:var(--blue);flex:none;border-radius:2px}
.feature b{color:var(--red);display:block;font-size:6.8px}
</style>
</head>
<body>
<main class="stage">

  <section class="spread">
    <article class="panel">
      <header class="head"><span class="tab">Files to BACKUP</span></header>
      <div class="body">
        <h3>What You Should Back Up?</h3>
        <p>You never have to worry about which files to protect. Back up the data your business relies on every day, stored safely offsite.</p>
        <div class="photo" role="img" aria-label="Photo of business team in an office"></div>
        <ul class="links">
          <li>Back up everything on your servers</li>
          <li>Back up your databases and mail</li>
          <li>Back up shared documents and files</li>
          <li>Back up accounting records</li>
          <li>Back up laptops and desktops</li>
          <li>Back up customer and sales data</li>
          <li>Back up photos, plans and designs</li>
          <li>Back up remote office computers</li>
          <li>Back up system settings and images</li>
        </ul>
      </div>
      <footer class="band"><span class="small">Why Use PlumVault?</span><span class="big">FILES TO BACKUP</span></footer>
    </article>

    <article class="panel mid">
      <div class="body">
        <ul class="bullets">
          <li>256 bit encryption for ultimate security</li>
          <li>Fast online recovery of any version of any protected file</li>
          <li>Easy Installation and setup</li>
          <li>Completely automated offsite-protection</li>
          <li>High speed internet is all that is required.</li>
        </ul>
        <div class="contact">
          <h3>Contact Us Today</h3>
          <div class="row"><span class="lbl">Phone</span><span>555-010-4477</span></div>
          <div class="row"><span class="lbl">Cell</span><span>555-010-2290</span></div>
          <div class="row"><span class="lbl">Fax</span><span>555-010-7104</span></div>
          <p><b>Address</b><br>482 Haverlund Corporate Park</p>
          <p><b>E-mail</b><br>darren@plumvault.example</p>
          <p><b>www.plumvault.example</b></p>
        </div>
      </div>
      <footer class="band black"><span class="small">CALL US NOW - Toll Free</span><span class="big tollfree">1 (555) 010-4477</span></footer>
    </article>

    <article class="panel cover">
      <div class="top"><span class="logo-mark"></span><span class="logo-name">PlumVault</span></div>
      <div class="slogan">
        <div class="s1">Protect YOUR</div>
        <div class="s2">BUSINESS</div>
        <div class="s3">with offsite data</div>
        <div class="s2">BACKUP</div>
      </div>
      <div class="globe-area" role="img" aria-label="Illustration of a blue globe"></div>
      <div class="url">http://www.plumvault.example</div>
      <footer class="band badge-band">
        <span class="circle247">24/7</span>
        <span class="small">SAFEGUARD YOUR DATA WITH THE ULTIMATE PEACE OF MIND</span>
      </footer>
    </article>
  </section>

  <section class="spread">
    <article class="panel">
      <header class="head"><span class="dot"></span><span class="tab dark">Why <b>BU?</b></span></header>
      <div class="body">
        <h3>PlumVault: The Best Backup Solution</h3>
        <p>PlumVault is the most reliable way to protect your data. Our remote managed service runs quietly in the background.</p>
        <div class="icons" role="img" aria-label="Grid of device and file icons">
          <span></span><span></span><span></span><span></span>
          <span></span><span></span><span></span><span></span>
          <span></span><span></span><span></span><span></span>
        </div>
        <p>Files are encrypted before they leave your office and stored in secure data centers.</p>
        <h4>Main Features</h4>
        <ul class="ticks">
          <li>Automatic daily schedules with no user action</li>
          <li>Full version history for every protected file</li>
          <li>Fast restore of single files or whole systems</li>
          <li>Detailed reports for every protected machine</li>
          <li>Monitoring by our support team around the clock</li>
          <li>Works with servers, desktops and laptops</li>
        </ul>
        <h4>Why Choose Us</h4>
        <p>We manage the whole process for you, so your staff can stay focused on running the business while your data stays safe.</p>
        <p>Setup takes minutes and our team checks every backup job to make sure your files can always be restored.</p>
      </div>
      <footer class="band black"><span class="small">The Best Backup Solution</span><span class="big">FILES TO BACKUP</span></footer>
    </article>

    <article class="panel">
      <header class="head"><span class="dot"></span><span class="tab dark">Data loss <b>RISKS</b></span></header>
      <div class="body">
        <h3>Guard Against Data loss Risks</h3>
        <p>To safeguard your data from all kinds of loss, you need an offsite copy that is always current and ready to restore.</p>
        <div class="risk"><span class="sq"></span><div><b>Protection from Hardware Failure</b>Drives fail without warning. Restore any file in minutes from our servers.</div></div>
        <div class="risk"><span class="sq"></span><div><b>Protection from Theft</b>Stolen laptops and servers no longer mean lost business records.</div></div>
        <div class="risk"><span class="sq"></span><div><b>Protection from Fire and Flood</b>Your data stays safe even when your office does not.</div></div>
        <div class="risk"><span class="sq"></span><div><b>Protection from Viruses</b>Roll back to clean versions saved before an attack.</div></div>
        <div class="risk"><span class="sq"></span><div><b>Protection from Human Error</b>Recover deleted or overwritten files from any date.</div></div>
        <div class="risk"><span class="sq"></span><div><b>Protection from Power Loss</b>Sudden outages cannot corrupt your offsite copies.</div></div>
        <div class="risk"><span class="sq"></span><div><b>Protection from Software Faults</b>Bad updates and crashes are undone with a quick restore.</div></div>
        <p>Most small firms that lose their data never fully recover. An offsite backup is the simplest way to keep your business running.</p>
      </div>
      <footer class="band"><span class="small">Guard against data loss RISKS</span><span class="big">FILES TO BACKUP</span></footer>
    </article>

    <article class="panel">
      <header class="head"><span class="dot"></span><span class="tab dark">Type of <b>USERS</b></span></header>
      <div class="body">
        <h3>Backup Software Features</h3>
        <p>Our award winning software gives every type of user the tools they need to keep data safe.</p>
        <div class="feature"><span class="sq"></span><div><b>Online Backup</b>Secure transfer to remote servers.</div></div>
        <div class="feature"><span class="sq"></span><div><b>Version Control</b>Keep every change of every file.</div></div>
        <div class="feature"><span class="sq"></span><div><b>Open File Backup</b>Protect files while in use.</div></div>
        <div class="feature"><span class="sq"></span><div><b>Email Alerts</b>Know the status of each job.</div></div>
        <div class="feature"><span class="sq"></span><div><b>Bandwidth Control</b>Run backups without slowing work.</div></div>
        <div class="feature"><span class="sq"></span><div><b>Quick Restore</b>Recover data in a few clicks.</div></div>
        <div class="feature"><span class="sq"></span><div><b>Database Support</b>Back up live mail and databases.</div></div>
        <div class="feature"><span class="sq"></span><div><b>Compression</b>Smaller uploads and faster jobs.</div></div>
        <div class="feature"><span class="sq"></span><div><b>Web Access</b>Reach your files from anywhere.</div></div>
        <div class="feature"><span class="sq"></span><div><b>Central Console</b>Manage all machines in one place.</div></div>
      </div>
      <footer class="band black"><span class="small">Backup Software Features</span><span class="big">FILES TO BACKUP</span></footer>
    </article>
  </section>

</main>
</body>
</html>
```